Kitchen manufaturer business card/logo design

I am a small kitchen manufacturing company that makes and installs all sorts of cabinetry.

The colours im looking to incorporate in the card are light/baby blue, white and black.

Incorporate 5 stars to show quality workmanship and product.

Looking for a modern classy design.
Updates

Hey guys, New idea. The logo should be made using HK in the most modern way possible as well as the full company name below it. Thanks.

Target Market(s)

Anyone with a home thats looking for a new cabinetry of any sort.

Industry/Entity Type

Business

Contact Information for Business Card

Harbor Kitchens
Ted Lowther
PH 0491 358 902
Email- harborkitchens@mailvane.example
ABN- 83 507 962 318
-Kitchens
-Vanities
-Laundries
-Media Units
-Studies
-Wardrobes
-3D Computer Designs

Requirements
Must have

• The front of the card must only have the company name.
The different types of cabinetry I do must be on the back of the card in point form but instead of using points use stars.
Nice to have
• Just think classy and quality

```html
<!DOCTYPE html>
<html lang="en">
<head>
<meta charset="utf-8">
<title>Harbor Kitchens – Business Card</title>
<link rel="stylesheet" href="https://fonts.googleapis.com/css2?family=Questrial&display=swap">
<style>
  :root {
    --canvas: #e9e9ee;
    --card-dark: #333333;
    --card-light: #f4f5f8;
    --navy: #0d3f8f;
    --blue: #0a73c4;
    --sky: #1ca3e6;
    --band-edge: #d7dde6;
    --ink: #3a3a3a;
    --white: #ffffff;
  }
  * { box-sizing: border-box; margin: 0; padding: 0; }
  html, body {
    width: 1200px; height: 934px; overflow: hidden;
    background: var(--canvas);
    font-family: "Questrial", "Century Gothic", sans-serif;
  }
  .stage {
    width: 1200px; height: 934px;
    display: flex; flex-direction: column;
    align-items: center; justify-content: center; gap: 44px;
  }
  .card {
    width: 620px; height: 378px; position: relative; overflow: hidden;
    box-shadow: 0 6px 18px rgba(0,0,0,0.12);
  }
  /* Front */
  .card-front {
    background: var(--card-dark);
    display: flex; align-items: center; justify-content: center;
  }
  .brand-name {
    color: var(--white); font-size: 38px; letter-spacing: 3px;
    text-transform: uppercase;
  }
  /* Back */
  .card-back { background: var(--card-light); }
  .service-band {
    position: absolute; left: 0; top: 0; width: 100%; height: 168px;
    background: linear-gradient(100deg, var(--navy) 0%, var(--blue) 55%, var(--sky) 100%);
    border-bottom: 6px solid var(--band-edge);
  }
  .service-list {
    position: absolute; left: 40px; top: 50px;
    display: grid; grid-template-columns: 118px 200px; row-gap: 14px;
    list-style: none;
  }
  .service-list li {
    color: var(--white); font-size: 15px; letter-spacing: 1px;
    text-transform: uppercase; display: flex; align-items: center;
  }
  .service-list li.starred::before {
    content: "★"; font-size: 9px; margin-right: 16px;
  }
  .person-name {
    position: absolute; right: 36px; top: 198px;
    color: var(--ink); font-size: 28px; letter-spacing: 1px;
    text-transform: uppercase;
  }
  .contact-list {
    position: absolute; left: 40px; bottom: 40px; list-style: none;
  }
  .contact-list li {
    display: flex; align-items: center; gap: 8px;
    color: var(--ink); font-size: 15px; letter-spacing: 0.3px; margin-top: 6px;
  }
  .contact-icon { width: 16px; height: 16px; flex: none; }
</style>
</head>
<body>
  <main class="stage">
    <section class="card card-front" aria-label="Card front">
      <h1 class="brand-name">Harbor Kitchens</h1>
    </section>

    <section class="card card-back" aria-label="Card back">
      <div class="service-band">
        <ul class="service-list">
          <li>Kitchens</li><li class="starred">Studies</li>
          <li>Vanities</li><li class="starred">Wardrobes</li>
          <li>Laundries</li><li class="starred">3D Computer Designs</li>
        </ul>
      </div>

      <p class="person-name">Ted Lowther</p>

      <ul class="contact-list">
        <li>
          <svg class="contact-icon" viewBox="0 0 16 16" aria-hidden="true">
            <rect width="16" height="16" rx="2" fill="#0a73c4"/>
            <path d="M5 3.5l2 2-1.2 1.3c.6 1.3 1.6 2.3 2.9 2.9L10 8.5l2 2-1.3 1.8C7 12 4 9 3.7 5.3z" fill="#fff"/>
          </svg>
          0491 358 902
        </li>
        <li>
          <svg class="contact-icon" viewBox="0 0 16 16" aria-hidden="true">
            <rect width="16" height="16" rx="2" fill="#0a73c4"/>
            <rect x="3" y="4.5" width="10" height="7" fill="none" stroke="#fff" stroke-width="1.2"/>
            <path d="M3 4.5l5 4 5-4" fill="none" stroke="#fff" stroke-width="1.2"/>
          </svg>
          harborkitchens@mailvane.example
        </li>
      </ul>
    </section>
  </main>
</body>
</html>
```